HARBORLINE BANK Stationery and BRAND ARCHITECTURE

We need a unique Design and Architecture for:

a. Business Card
b. Letterhead
c. Continuation Sheet
d. Envelope
e. Email Signature
f. Complimentary Slip
g. Poster
h. Corporate Folder

1. Information for the call card:

Marcus J. Okafor
Senior Assistant Managing Director
General Banking Division
Harborline Bank
P.O. Box 517, Palmetto Lane, Basseterre, St. Kitts, West Indies
Office.: (869) 555-0148 Ext 2207
M.: (869) 555-0193
F.: (869) 555-0176
Email: marcusokafor@harborlinebankexample.com
harborlinebank.example

2. All pieces must include:
a. Address
b. Contact info
c.twitter and Facebook address

The Information for the posters:
Visual:A Happy Black Family
Headline Our future together – Better!
Bold Our People know how to build for the long term. How to root the future firmly in the strengths of our people.
A Harbor we can lean on for the better!

Target Market(s)

BUSiness
Bank Customers

Industry/Entity Type

Bank

Requirements
Must have
• - Logo wiht tag
• - use of Logo Colours
• - Green and Red as main colours but the yellow and black are also important
• - the red circles MUSt be used inthe brand architecture

```html
<!DOCTYPE html>
<html lang="en">
<head>
<meta charset="utf-8">
<title>Harborline Bank – Business Card</title>
<link href="https://fonts.googleapis.com/css2?family=Raleway:wght@400;500;700&display=swap" rel="stylesheet">
<style>
  :root{
    --bg:#151515;
    --paper:#f7f7f5;
    --green:#1e5a2a;
    --green-dark:#1a4f25;
    --red:#c4262e;
    --yellow:#e8b518;
    --ink:#2b2b2b;
    --white:#ffffff;
  }
  *{margin:0;padding:0;box-sizing:border-box}
  html,body{width:1200px;height:1001px;overflow:hidden;background:var(--bg)}
  body{position:relative;font-family:"Raleway",sans-serif;color:var(--ink)}

  .card{position:absolute;width:589px;height:330px;overflow:hidden}
  .card-front{left:203px;top:132px;background:var(--paper)}
  .card-back{left:408px;top:539px;background:var(--green)}

  .holder-name{position:absolute;left:36px;top:78px;font-weight:700;font-size:18px;letter-spacing:.3px;color:var(--green)}
  .holder-title{position:absolute;left:36px;top:100px;font-size:14px;font-weight:400}

  .contact-list{position:absolute;left:36px;top:151px;list-style:none}
  .contact-list li{display:flex;align-items:center;height:18.5px;font-size:14px}
  .contact-list svg{width:15px;height:15px;margin-right:10px;flex:none}

  .address{position:absolute;left:36px;top:233px;font-size:14px;line-height:19px}

  .brand{position:absolute;text-align:center}
  .brand-front{left:339px;top:34px;width:210px}
  .brand-dot{display:block;margin:0 auto;border-radius:50%;background:var(--red)}
  .brand-front .brand-dot{width:26px;height:26px;margin-bottom:8px}
  .brand-name{font-weight:700;white-space:nowrap;line-height:1}
  .brand-front .brand-name{font-size:28px;color:var(--green)}
  .brand-tag{font-weight:500;white-space:nowrap}
  .brand-front .brand-tag{font-size:14px;color:#222;margin-top:4px}

  .band{position:absolute;top:293px;height:18px}
  .band-green{left:0;width:445px;background:var(--green)}
  .band-yellow{left:445px;right:0;background:var(--yellow)}
  .band-dot{position:absolute;left:442px;top:288px;width:28px;height:28px;border-radius:50%;background:var(--red);border:5px solid var(--paper)}

  .brand-back{left:228px;top:160px;width:340px}
  .brand-back .brand-dot{width:32px;height:32px;margin-bottom:12px}
  .brand-back .brand-name{font-size:40px;color:var(--white)}
  .brand-back .brand-tag{font-size:19px;color:var(--white);margin-top:4px}
</style>
</head>
<body>

<section class="card card-front" aria-label="Business card front">
  <div class="holder-name">MARCUS J. OKAFOR</div>
  <div class="holder-title">Senior Assistant Managing Director</div>

  <ul class="contact-list">
    <li>
      <svg viewBox="0 0 16 16" aria-hidden="true"><rect width="16" height="16" rx="3" fill="var(--red)"/><path d="M5 3.5c.6-.3 1.2 0 1.4.6l.5 1.4c.2.5 0 1-.4 1.2l-.6.4c.6 1.3 1.5 2.2 2.8 2.8l.4-.6c.3-.4.8-.6 1.2-.4l1.4.5c.6.2.9.8.6 1.4-.5 1.1-1.6 1.6-2.8 1.2C7 11.2 4.8 9 4 6.3c-.4-1.2.1-2.3 1-2.8z" fill="#fff"/></svg>
      (869) 555-0148 Ext 2207
    </li>
    <li>
      <svg viewBox="0 0 16 16" aria-hidden="true"><rect width="16" height="16" rx="3" fill="var(--red)"/><rect x="5" y="3" width="6" height="10" rx="1.2" fill="none" stroke="#fff" stroke-width="1.4"/><rect x="6.5" y="4.6" width="3" height="5" fill="#fff"/></svg>
      (869) 555-0193
    </li>
    <li>
      <svg viewBox="0 0 16 16" aria-hidden="true"><rect width="16" height="16" rx="3" fill="var(--red)"/><rect x="3.5" y="5" width="9" height="6.5" fill="none" stroke="#fff" stroke-width="1.2"/><path d="M3.5 5l4.5 3.5L12.5 5" fill="none" stroke="#fff" stroke-width="1.2"/></svg>
      marcusokafor@harborlinebankexample.com
    </li>
    <li>
      <svg viewBox="0 0 16 16" aria-hidden="true"><rect width="16" height="16" rx="3" fill="var(--red)"/><circle cx="8" cy="8" r="4.6" fill="none" stroke="#fff" stroke-width="1.1"/><ellipse cx="8" cy="8" rx="2" ry="4.6" fill="none" stroke="#fff" stroke-width="1"/><path d="M3.4 8h9.2" stroke="#fff" stroke-width="1"/></svg>
      www.harborlinebankexample.com
    </li>
  </ul>

  <address class="address" style="font-style:normal">
    P.O. Box 517, Palmetto Lane<br>
    Basseterre, St. Kitts, West Indies
  </address>

  <div class="brand brand-front">
    <span class="brand-dot"></span>
    <div class="brand-name">Harborline Bank</div>
    <div class="brand-tag">Lean On Better</div>
  </div>

  <div class="band band-green"></div>
  <div class="band band-yellow"></div>
  <span class="band-dot"></span>
</section>

<section class="card card-back" aria-label="Business card back">
  <div class="brand brand-back">
    <span class="brand-dot"></span>
    <div class="brand-name">Harborline Bank</div>
    <div class="brand-tag">Lean On Better</div>
  </div>
</section>

</body>
</html>
```